Australian IT Company requires Business Card Design

Bluewattle is an Australian company that specialises in IT consulting & support, software development, project management, network services.

We have been in business for 15 years.

* We require a business card with the following on it:
Logo
Address
Contact Details
Space for staff name, title & mobile number

Industry/Entity Type

Software

```html
<!DOCTYPE html>
<html lang="en">
<head>
<meta charset="utf-8">
<title>Bluewattle Business Card</title>
<link rel="stylesheet" href="https://fonts.googleapis.com/css2?family=Arimo:wght@400;700&display=swap">
<style>
  :root {
    --backdrop: #d9dcdd;
    --card: #ffffff;
    --brand-blue: #2f6db5;
    --ink-grey: #5a5d60;
    --shadow: rgba(0, 0, 0, 0.18);
  }
  * { margin: 0; padding: 0; box-sizing: border-box; }
  html, body {
    width: 1200px;
    height: 1200px;
    overflow: hidden;
    background: var(--backdrop);
  }
  .stage {
    width: 1200px;
    height: 1200px;
    display: flex;
    align-items: center;
    justify-content: center;
  }
  .business-card {
    position: relative;
    width: 1000px;
    height: 580px;
    background: var(--card);
    box-shadow: 0 14px 40px var(--shadow);
    overflow: hidden;
    font-family: "Arimo", Arial, sans-serif;
  }
  .company {
    position: absolute;
    left: 70px;
    top: 190px;
    display: flex;
    align-items: center;
    gap: 16px;
  }
  .company-dot {
    width: 22px;
    height: 22px;
    border-radius: 50%;
    background: var(--brand-blue);
  }
  .company-name {
    font-size: 44px;
    font-weight: 700;
    color: var(--brand-blue);
    line-height: 1;
  }
  .staff {
    position: absolute;
    left: 150px;
    top: 290px;
    display: flex;
    flex-direction: column;
    align-items: flex-end;
  }
  .staff-name {
    font-size: 36px;
    font-weight: 700;
    color: var(--ink-grey);
    letter-spacing: 7px;
  }
  .staff-title {
    font-size: 19px;
    font-weight: 700;
    color: var(--brand-blue);
    letter-spacing: 2px;
    margin-top: -2px;
  }
  .contact-list {
    position: absolute;
    left: 70px;
    bottom: 56px;
    list-style: none;
    font-size: 22px;
    font-weight: 700;
    line-height: 1.32;
    color: var(--ink-grey);
    letter-spacing: 1px;
  }
  .contact-label { color: var(--brand-blue); }
</style>
</head>
<body>
  <main class="stage">
    <article class="business-card">
      <header class="company">
        <span class="company-dot" aria-hidden="true"></span>
        <span class="company-name">Bluewattle</span>
      </header>

      <section class="staff">
        <span class="staff-name">Your Name</span>
        <span class="staff-title">Title</span>
      </section>

      <ul class="contact-list">
        <li><span class="contact-label">T:</span> +61 3 9555 0182</li>
        <li><span class="contact-label">E:</span> staff members email address</li>
        <li><span class="contact-label">W:</span> www.bluewattle.net.au</li>
        <li><span class="contact-label">A:</span> 14 Ridge Lane Tech Building 3 Kingsbury Vic 3085</li>
      </ul>
    </article>
  </main>
</body>
</html>
```